Sticker label design for - Over Fleet Deodorant Balm

I need a label for my 100% Natural Deodorant Balm
The brand is called "Mild Meadow Brand", and the product is called OVER FLEET Deodorant Balm.
There are two labels, one is a 5.2cm circle for the top, and 4.5cm circle for the base. The jar is amber plastic with black lid.
Width: 5.8cm
Height: 3.4cm (Lid 1.2cm, base 2,2cm)
Here is a link to what the jar looks like from one of my competitors: https://redsparrow.com.au/products/body/crest-deodorant-paste/
The product is a unisex product. Please see uploaded files for designs previously made for the brand. I'm trying to see a few more designs before finalising my choice. Feel free to use the logo at the top (Mild Meadow Brand) of either attachment if you would like. Or design your own.
Be be aware that it is meant to be Aluminium and Paraben Free, not "Parabens" Weight of product is 70g, please include this.
Label can be any colour, and printed with regular colours or event gold, silver or rose gold foil. Would a background be nice?
This is something I saw that I liked:
http://www.tolvenbalm.com
However I'm really open to what people can come up with.
For the back base-
Over Fleet deodorant balm is made from 100% natural ingredients, and works by neutralises odour and minimising wetness without the use of harmful chemicals.
www.mildmeadowbrand.com
Directions: For optimal result, apply a pea size amount of the balm to your dry armpits. Gently rub the balm into your armpits covering the entire area. Discontinue use if irritation occurs.
Ingredients: Shea Butter, Coconut oil, Sodium Bicarbonate, Arrowroot, Kaolin Clay, Vitamin E, Vegetable Glycerin, Activated Charcoal, Essential oils of Peppermint, Lavender, Mandarin, Tea tree, Geranium Rose & Cedarwood.
MADE IN AUSTRALIA
Reason: Hi,
I'm not getting many submissions, so was hoping to extend the deadline.
Skin Care Product

```html
<!DOCTYPE html>
<html lang="en">
<head>
<meta charset="utf-8">
<title>Over Fleet Deodorant Balm – Label Set</title>
<link href="https://fonts.googleapis.com/css2?family=Delius&family=Open+Sans:wght@400;700&family=Montserrat:wght@800&display=swap" rel="stylesheet">
<style>
  :root{
    --stage:#6b6b6b;
    --paper:#e9e9e9;
    --ink:#474747;
    --ink-dark:#3a3a3a;
    --white:#f7f7f7;
  }
  *{margin:0;padding:0;box-sizing:border-box}
  html,body{width:1200px;height:802px;overflow:hidden;background:var(--stage)}
  .sheet{position:relative;width:1200px;height:802px}

  .label{position:absolute;display:flex;flex-direction:column;align-items:center;justify-content:center;text-align:center}
  .label svg.shape{position:absolute;inset:0;width:100%;height:100%}
  .label .content{position:relative;display:flex;flex-direction:column;align-items:center}

  .lid{width:350px;height:350px;top:50px}
  .lid--light{left:155px}
  .lid--dark{left:695px}
  .body{width:370px;height:240px;top:500px}
  .body--light{left:145px}
  .body--dark{left:685px}

  .brand{font-family:"Open Sans",sans-serif;font-weight:700;letter-spacing:.06em;display:flex;align-items:center;gap:6px}
  .brand-dot{width:7px;height:7px;border-radius:50%;background:currentColor}
  .product{font-family:"Delius",cursive;line-height:1}
  .subtitle{font-family:"Open Sans",sans-serif;font-weight:400}
  .claims{font-family:"Open Sans",sans-serif;font-weight:700;letter-spacing:.03em;line-height:1.35;text-transform:uppercase}
  .natural{font-family:"Montserrat",sans-serif;font-weight:800;letter-spacing:.04em;transform:rotate(-5deg)}

  .lid .brand{font-size:11px;margin-bottom:22px}
  .lid .product{font-size:46px}
  .lid .subtitle{font-size:17px;margin-bottom:12px}
  .lid .claims{font-size:10.5px}
  .lid .natural{font-size:21px;margin-top:4px}

  .body .brand{font-size:9px;margin-bottom:8px}
  .body .product{font-size:34px}
  .body .subtitle{font-size:13px;margin-bottom:6px}
  .body .claims{font-size:7.5px}
  .body .natural{font-size:12px;margin-top:4px}

  .on-light{color:var(--ink)}
  .on-dark{color:var(--white)}
</style>
</head>
<body>
<main class="sheet">

  <section class="label lid lid--light on-light" aria-label="Lid label, light">
    <svg class="shape" viewBox="0 0 350 350" aria-hidden="true">
      <circle cx="175" cy="175" r="175" fill="var(--paper)"/>
      <circle cx="175" cy="175" r="152" fill="none" stroke="var(--ink)" stroke-width="16"/>
    </svg>
    <div class="content">
      <div class="brand"><span class="brand-dot"></span>MILD MEADOW BRAND</div>
      <div class="product">Over Fleet</div>
      <div class="subtitle">Deodorant Balm</div>
      <div class="claims">Aluminium &amp; Paraben Free<br>Vegan<br>Cruelty Free</div>
      <div class="natural">%100 NATURAL</div>
    </div>
  </section>

  <section class="label lid lid--dark on-dark" aria-label="Lid label, dark">
    <svg class="shape" viewBox="0 0 350 350" aria-hidden="true">
      <circle cx="175" cy="175" r="175" fill="var(--paper)"/>
      <circle cx="175" cy="175" r="160" fill="none" stroke="var(--ink)" stroke-width="3"/>
      <circle cx="175" cy="175" r="150" fill="var(--ink-dark)"/>
      <circle cx="175" cy="175" r="142" fill="none" stroke="var(--white)" stroke-width="2"/>
    </svg>
    <div class="content">
      <div class="brand"><span class="brand-dot"></span>MILD MEADOW BRAND</div>
      <div class="product">Over Fleet</div>
      <div class="subtitle">Deodorant Balm</div>
      <div class="claims">Aluminium &amp; Paraben Free<br>Vegan<br>Cruelty Free</div>
      <div class="natural">%100 NATURAL</div>
    </div>
  </section>

  <section class="label body body--light on-light" aria-label="Jar label, light">
    <svg class="shape" viewBox="0 0 370 240" aria-hidden="true">
      <path d="M26,0 H344 A26,26 0 0 0 370,26 V214 A26,26 0 0 0 344,240 H26 A26,26 0 0 0 0,214 V26 A26,26 0 0 0 26,0 Z" fill="var(--paper)"/>
      <path d="M36,10 H334 A26,26 0 0 0 360,36 V204 A26,26 0 0 0 334,230 H36 A26,26 0 0 0 10,204 V36 A26,26 0 0 0 36,10 Z" fill="none" stroke="var(--ink)" stroke-width="3"/>
      <path d="M44,18 H326 A22,22 0 0 0 352,44 V196 A22,22 0 0 0 326,222 H44 A22,22 0 0 0 18,196 V44 A22,22 0 0 0 44,18 Z" fill="none" stroke="var(--ink)" stroke-width="1.2"/>
    </svg>
    <div class="content">
      <div class="brand"><span class="brand-dot"></span>MILD MEADOW BRAND</div>
      <div class="product">Over Fleet</div>
      <div class="subtitle">Deodorant Balm</div>
      <div class="claims">Aluminium &amp; Paraben Free<br>Vegan<br>Cruelty Free</div>
      <div class="natural">%100 NATURAL</div>
    </div>
  </section>

  <section class="label body body--dark on-dark" aria-label="Jar label, dark">
    <svg class="shape" viewBox="0 0 370 240" aria-hidden="true">
      <path d="M26,0 H344 A26,26 0 0 0 370,26 V214 A26,26 0 0 0 344,240 H26 A26,26 0 0 0 0,214 V26 A26,26 0 0 0 26,0 Z" fill="var(--ink-dark)"/>
      <path d="M36,10 H334 A26,26 0 0 0 360,36 V204 A26,26 0 0 0 334,230 H36 A26,26 0 0 0 10,204 V36 A26,26 0 0 0 36,10 Z" fill="none" stroke="var(--white)" stroke-width="2"/>
    </svg>
    <div class="content">
      <div class="brand"><span class="brand-dot"></span>MILD MEADOW BRAND</div>
      <div class="product">Over Fleet</div>
      <div class="subtitle">Deodorant Balm</div>
      <div class="claims">Aluminium &amp; Paraben Free<br>Vegan<br>Cruelty Free</div>
      <div class="natural">%100 NATURAL</div>
    </div>
  </section>

</main>
</body>
</html>
```